Stationary Set Rebrand for Brenton

We are a Canadian Distribution and Service Company that was established in 1969. Over the past 5 decades we have expanded our business and have warehouses across Canada. We specialize in adhesive tapes, adhesives, films, safety, warehouse, shipping, janitorial and packaging supplies.

We have updated our logo design and would like a new corporate branding identity that includes a new fresh Stationary Set (Business Cards, Letterhead, Letterhead MS Word, Envelope, Presentation Folders, Email Signatures, Notepad Covers, etc.)

Target Market(s)

Industrial Business Sector

Font styles to use
Sans Serif

Colors
0054AA
0677BA
7BADD7
CADEEF
E8F1F8
0094D4
00A9DD
6FCCEA
C7EBF8
E9F6FB
00AB8E
00BBA5
67D7C9
C6EFE9
E9F9F6
EB3D1F
EC4F4E
F09395
F8D3D4
FCEDEE

Requirements
Should not have
• Colors not too light, darker colours preferred

```html
<!DOCTYPE html>
<html lang="en">
<head>
<meta charset="utf-8">
<title>Brenton Business Card</title>
<link rel="stylesheet" href="https://fonts.googleapis.com/css2?family=Archivo:wdth,wght@62..125,400;62..125,700;62..125,800&display=swap">
<style>
  :root {
    --backdrop: #e4e4e4;
    --card-white: #ffffff;
    --brand-red: #d71920;
    --ink: #1e1e1e;
    --text-grey: #4a4a4a;
    --divider: #b5b5b5;
  }
  * { margin: 0; padding: 0; box-sizing: border-box; }
  html, body { width: 1200px; height: 1200px; overflow: hidden; }
  body {
    position: relative;
    background: var(--backdrop);
    font-family: "Archivo", Arial, sans-serif;
  }
  .card {
    position: absolute;
    left: 252px;
    width: 696px;
    height: 398px;
    overflow: hidden;
  }
  .card-front { top: 150px; background: var(--card-white); }
  .card-back { top: 652px; background: var(--brand-red); }

  .wordmark {
    position: absolute;
    font-weight: 800;
    font-stretch: 125%;
    letter-spacing: -1px;
    line-height: 1;
  }
  .card-front .wordmark {
    left: 78px; top: 168px;
    font-size: 52px;
    color: var(--ink);
  }
  .card-back .wordmark {
    left: 0; right: 0; top: 148px;
    text-align: center;
    font-size: 84px;
    color: var(--card-white);
  }

  .divider {
    position: absolute;
    left: 362px; top: 99px;
    width: 2px; height: 202px;
    background: linear-gradient(to bottom, transparent, var(--divider) 15%, var(--divider) 85%, transparent);
  }

  .contact { position: absolute; left: 389px; top: 104px; color: var(--text-grey); }
  .contact-name {
    font-size: 27px;
    font-weight: 700;
    font-stretch: 125%;
    color: var(--brand-red);
    line-height: 1;
  }
  .contact-title { font-size: 15px; margin-top: 6px; letter-spacing: 0.5px; }
  .contact-address { font-size: 16px; line-height: 21px; margin-top: 20px; letter-spacing: 0.5px; }
  .contact-lines { list-style: none; margin-top: 12px; font-size: 16px; letter-spacing: 0.5px; }
  .contact-lines li { display: flex; align-items: center; height: 21px; }
  .contact-lines svg { width: 15px; height: 15px; margin-right: 11px; flex: none; }

  .footer-band { position: absolute; left: 0; top: 367px; width: 696px; height: 31px; }
  .website {
    position: absolute;
    left: 527px; top: 374px;
    font-size: 16px;
    letter-spacing: 0.5px;
    color: var(--card-white);
  }
</style>
</head>
<body>
  <section class="card card-front">
    <div class="wordmark">Brenton</div>
    <div class="divider"></div>
    <div class="contact">
      <div class="contact-name">DANA WHITFIELD</div>
      <div class="contact-title">President</div>
      <div class="contact-address">4120 Maple Ridge Road<br>Kelowna, Canada 52810</div>
      <ul class="contact-lines">
        <li>
          <svg viewBox="0 0 16 16" aria-hidden="true"><path fill="#d71920" d="M3.5 1 6 4.2 4.6 5.8c.9 2.2 2.7 4 5 5l1.5-1.4L14.5 12 13 14.8C7 14.5 1.5 9 1 3z"/></svg>
          555-214-7730
        </li>
        <li>
          <svg viewBox="0 0 16 16" aria-hidden="true"><rect x="4" y="1" width="8" height="14" rx="1.2" fill="none" stroke="#d71920" stroke-width="1.6"/><rect x="7" y="12" width="2" height="1.2" fill="#d71920"/></svg>
          555-390-6182
        </li>
        <li>
          <svg viewBox="0 0 16 16" aria-hidden="true"><rect x="1" y="3.5" width="14" height="9.5" fill="#d71920"/><path d="M1.5 4 8 9l6.5-5" fill="none" stroke="#fff" stroke-width="1.2"/></svg>
          info@brenton.com
        </li>
      </ul>
    </div>
    <svg class="footer-band" viewBox="0 0 696 31" aria-hidden="true">
      <path fill="#1e1e1e" d="M0 1H451L442 15H0Z"/>
      <path fill="#d71920" d="M458 0H696V31H0V19H440Q447 19 450 13L455 3Q456 0 458 0Z"/>
    </svg>
    <div class="website">www.brenton.com</div>
  </section>

  <section class="card card-back">
    <div class="wordmark">Brenton</div>
  </section>
</body>
</html>
```